Personal Business Card

Looking for a clean and modern personal business card. Basically I need something catchy to give to potential clients and people I meet. I do a lot of freelancing (from DJ'ing to wedding videography, but its mostly on the event side of things) so it's more-so about selling myself rather than identifying with a company. I'm starting to meet more people that I want to work with after meeting them so I'm revamping my business cards.

I'm looking for a clean and modern design- I know that's really vague but I'm fine with anything ranging from a symbol to just a fancy version of my name.

Details I need on the front:
Dennis Kowal
dennis@denniskowal-mail.net
(555) 807-2291

On the back I'd like to have something simple like "Nice to have met you today" or "Great meeting you".

UPDATE 9/27 Noon: My apologies for not putting it up before- I'm definitely looking for full color. Doesn't have to be a rainbow but I am looking for the least amount of blank white as possible.

UPDATE 10/1: Really impressed with what I've been getting so far and I'm working on giving everyone feedback- if your design is still up then you're still in the run. Looking for something more unique and modern so please do not post something that looks like a template from Cardloom!

Target Market(s)

Mainly to give to people aged 18-35. Most of my encounters will be casual so the card should have a "young" feeling to it. I rarely do anything in the corporate world so it doesn't have to be boring. It should give the impression that I'm the one they should go to if they need what I do (again it changes every weekend so I'll probably say the "what I do" part.

Industry/Entity Type

Wedding

Requirements
Must have
• Basically the contact information listed above
Nice to have
• I really like the colors Blue, Silver, and Purple. They don't have to necessarily all be there though. I do like the look of polished metal if that makes sense.
Should not have
• A template that resembles card-loom. I'm in a point in my life where I'm working a lot of different markets/areas so the card does not need to have an address or address placeholder.

```html
<!DOCTYPE html>
<html lang="en">
<head>
<meta charset="UTF-8">
<title>Dennis Kowal — Business Card</title>
<link rel="stylesheet" href="https://fonts.googleapis.com/css2?family=Great+Vibes&family=Pinyon+Script&family=Arimo&display=swap">
<style>
  :root {
    --page: #ffffff;
    --splash-sky: #cfe6fb;
    --splash-blue: #6f7df0;
    --splash-violet: #8a3fe0;
    --splash-magenta: #e03ab8;
    --splash-orange: #f0a55a;
    --band: rgba(255, 255, 255, 0.72);
    --ink-dark: #1b1b1b;
    --name-white: #ffffff;
    --handshake-grey: #b9b3b8;
    --handshake-rose: #e8bfd0;
    --handshake-pale: #f1dde6;
    --greeting-blue: #1f4fd8;
  }
  html, body {
    margin: 0;
    padding: 0;
    overflow: hidden;
    background: var(--page);
  }
  .canvas {
    position: relative;
    width: 1200px;
    height: 320px;
    background: var(--page);
    overflow: hidden;
  }
  .card-shapes {
    position: absolute;
    inset: 0;
  }
  .card-front, .card-back {
    position: absolute;
    top: 0;
    height: 320px;
  }
  .card-front { left: 0; width: 578px; }
  .card-back { left: 623px; width: 577px; }
  .front-name {
    position: absolute;
    left: 250px;
    top: 95px;
    margin: 0;
    font-family: "Great Vibes", cursive;
    font-weight: 400;
    font-size: 50px;
    color: var(--name-white);
    letter-spacing: 1px;
    text-shadow: 1px 1px 2px rgba(60, 20, 90, 0.35);
    white-space: nowrap;
  }
  .contact-band {
    position: absolute;
    left: 26px;
    top: 240px;
    width: 350px;
    height: 62px;
    background: var(--band);
  }
  .contact-list {
    position: absolute;
    left: 40px;
    top: 245px;
    margin: 0;
    padding: 0;
    list-style: none;
    font-family: "Arimo", Arial, sans-serif;
    font-size: 18px;
    line-height: 22px;
    color: var(--ink-dark);
  }
  .greeting {
    position: absolute;
    left: 68px;
    top: 162px;
    margin: 0;
    font-family: "Pinyon Script", cursive;
    font-weight: 400;
    font-size: 34px;
    color: var(--greeting-blue);
    white-space: nowrap;
    line-height: 1;
  }
  .greeting-initial {
    font-size: 118px;
    vertical-align: -2px;
    margin-left: 4px;
  }
</style>
</head>
<body>
  <main class="canvas">
    <svg class="card-shapes" width="1200" height="320" viewBox="0 0 1200 320" aria-hidden="false">
      <defs>
        <linearGradient id="splashFill" x1="0" y1="0" x2="1" y2="0.4">
          <stop offset="0" stop-color="var(--splash-magenta)"/>
          <stop offset="0.12" stop-color="var(--splash-orange)"/>
          <stop offset="0.3" stop-color="var(--splash-sky)"/>
          <stop offset="0.55" stop-color="var(--splash-blue)"/>
          <stop offset="0.8" stop-color="var(--splash-violet)"/>
          <stop offset="1" stop-color="var(--splash-magenta)"/>
        </linearGradient>
        <linearGradient id="handshakeFill" x1="0" y1="0" x2="1" y2="1">
          <stop offset="0" stop-color="var(--handshake-grey)"/>
          <stop offset="0.45" stop-color="var(--handshake-rose)"/>
          <stop offset="1" stop-color="var(--handshake-pale)"/>
        </linearGradient>
      </defs>
      <path class="front-artwork" role="img" aria-label="Colourful paint-splash artwork with a dancing figure in blue, purple, magenta and orange"
        d="M0,95 Q0,12 90,10 C200,6 260,62 360,56 C450,50 495,8 540,18 Q578,28 578,90 V320 H0 Z"
        fill="url(#splashFill)"/>
      <path class="back-artwork" role="img" aria-label="Soft faded photograph of two people shaking hands"
        d="M623,55 Q623,20 665,22 C735,26 785,62 855,56 C950,48 1005,2 1100,5 Q1200,10 1200,95 V320 H623 Z"
        fill="url(#handshakeFill)"/>
    </svg>

    <section class="card-front" aria-label="Card front">
      <h1 class="front-name">Dennis Kowal</h1>
      <div class="contact-band"></div>
      <ul class="contact-list">
        <li class="contact-email">dennis@denniskowal-mail.net</li>
        <li class="contact-phone">(555) 807-2291</li>
      </ul>
    </section>

    <section class="card-back" aria-label="Card back">
      <p class="greeting">Nice to have met you<span class="greeting-initial">T</span>oday</p>
    </section>
  </main>
</body>
</html>
```